Candle Box & Belly Band Design

Design Candle Box for Soy Candles along with a belly band design that can be used on off the shelf coloured boxes. It is for a premium brand of candle - so i want the packaging to reflect this. I have included must haves below.

The candle boxes will be a few different sizes, but for the purpose of the design it would be something like a cube 12 x 12 x 12 cms

The belly band for standard boxes to be something like 5cm wide on a 12 x 12 x 12cms cube box that goes all the way around the top to the bottom - holding the lid on and providing all the relevant information. Example of box with belly band uploaded

Our company Name : Hazel & Pip - our logo is uploaded

Target Market(s)

Premium Candle Buyers

Colors

Designer to choose colors to be used in the design.

Requirements
Must have
• Must have our logo - our logo can be in any colour
• Must state:
• Soy Candle, Hand Poured, Made in Melbourne,
• A space for the fragrance, size and burn time.
• For this project use Lime, Coconut & Elderfllower, 300grams, 50 Hour burn Time

```html
<!DOCTYPE html>
<html lang="en">
<head>
<meta charset="utf-8">
<title>Hazel &amp; Pip Soy Candle Box and Belly Band</title>
<link rel="stylesheet" href="https://fonts.googleapis.com/css2?family=Barlow:wght@400;500;600&family=Barlow+Condensed:wght@600&display=swap">
<style>
  :root {
    --backdrop: #b6b7ba;
    --box-charcoal: #454545;
    --box-white: #e9e9e9;
    --band-lime: #bccb12;
    --ink: #141414;
    --brand-pink: #f0318a;
  }
  * { box-sizing: border-box; margin: 0; padding: 0; }
  html, body { width: 1200px; height: 873px; overflow: hidden; }
  body {
    background: var(--backdrop);
    font-family: "Barlow", sans-serif;
    position: relative;
  }
  .box-face {
    position: absolute;
    top: 216px;
    width: 440px;
    height: 440px;
  }
  .box-face--charcoal { left: 120px; background: var(--box-charcoal); }
  .box-face--white { left: 640px; background: var(--box-white); }

  .belly-band {
    position: absolute;
    top: 0;
    left: 44px;
    width: 118px;
    height: 100%;
    background: var(--band-lime);
    color: var(--ink);
    display: flex;
    flex-direction: column;
    align-items: center;
    text-align: center;
    padding: 26px 8px 22px;
  }
  .band-tagline {
    font-size: 13px;
    line-height: 1.2;
    letter-spacing: 0.02em;
  }
  .band-brand {
    margin-top: 52px;
    font-size: 19px;
    font-weight: 500;
    line-height: 1.1;
  }
  .band-fragrance {
    margin-top: 52px;
    font-size: 15px;
    font-weight: 500;
    line-height: 1.15;
  }
  .band-size {
    margin-top: 22px;
    font-size: 14px;
    font-weight: 500;
    line-height: 1.1;
  }
  .band-origin {
    margin-top: 18px;
    font-size: 11px;
    line-height: 1.2;
    letter-spacing: 0.03em;
    text-transform: uppercase;
  }
  .band-burn {
    margin-top: auto;
    display: flex;
    align-items: center;
    gap: 3px;
  }
  .burn-hours {
    font-family: "Barlow Condensed", sans-serif;
    font-weight: 600;
    font-size: 40px;
    line-height: 1;
  }
  .burn-label {
    font-size: 9px;
    line-height: 1.05;
    text-align: left;
  }
  .burn-label strong { font-weight: 600; font-size: 10px; }

  .face-brand {
    position: absolute;
    left: 200px;
    right: 10px;
    top: 150px;
    color: var(--brand-pink);
    text-align: center;
    display: flex;
    flex-direction: column;
    align-items: center;
  }
  .brand-dot {
    width: 26px;
    height: 26px;
    border-radius: 50%;
    background: var(--brand-pink);
    margin-bottom: 14px;
  }
  .face-brand-name {
    font-size: 30px;
    font-weight: 500;
    line-height: 1.1;
  }
  .face-brand-tagline {
    margin-top: 6px;
    font-size: 17px;
    line-height: 1.1;
    letter-spacing: 0.03em;
  }
</style>
</head>
<body>
  <section class="box-face box-face--charcoal">
    <div class="belly-band">
      <p class="band-tagline">SOY CANDLE<br>Hand Poured</p>
      <p class="band-brand">Hazel &amp; Pip</p>
      <p class="band-fragrance">Lime<br>Coconut &amp;<br>Elderflower</p>
      <p class="band-size">300 grams</p>
      <p class="band-origin">Made in<br>Melbourne</p>
      <div class="band-burn">
        <span class="burn-hours">50</span>
        <span class="burn-label"><strong>HRS</strong><br>Burn<br>Time</span>
      </div>
    </div>
    <div class="face-brand">
      <span class="brand-dot"></span>
      <p class="face-brand-name">Hazel &amp; Pip</p>
      <p class="face-brand-tagline">SOY CANDLE<br>Hand Poured</p>
    </div>
  </section>

  <section class="box-face box-face--white">
    <div class="belly-band">
      <p class="band-tagline">SOY CANDLE<br>Hand Poured</p>
      <p class="band-brand">Hazel &amp; Pip</p>
      <p class="band-fragrance">Lime<br>Coconut &amp;<br>Elderflower</p>
      <p class="band-size">300 grams</p>
      <p class="band-origin">Made in<br>Melbourne</p>
      <div class="band-burn">
        <span class="burn-hours">50</span>
        <span class="burn-label"><strong>HRS</strong><br>Burn<br>Time</span>
      </div>
    </div>
    <div class="face-brand">
      <span class="brand-dot"></span>
      <p class="face-brand-name">Hazel &amp; Pip</p>
      <p class="face-brand-tagline">SOY CANDLE<br>Hand Poured</p>
    </div>
  </section>
</body>
</html>
```